IT services company needs a business card designed

-2 sided business card.-Front is going to be the logo raised (3D floating effect) on a black background. Make the logos spider web shiny silver and keep the spider the same design. -Back needs to have the following information:Darrel Sotho, Managing Partner, Cell: 738-402-1954, Website: Plankhorn.com, Email: Darrel@Plankhorn.com
Target Market(s)
IT Services
Industry/Entity Type
It Company
Contact Information for Business Card
-2 sided business card.
-Front is going to be the logo raised (3D floating effect) on a black background. Make the logos spider web shiny silver and keep the spider the same design.
-Back needs to have the following information:
Darrel Sotho, Managing Partner, Cell: 738-402-1954, Website: Plankhorn.com, Email: Darrel@Plankhorn.com

```html
<!DOCTYPE html>
<html lang="en">
<head>
<meta charset="UTF-8">
<title>Plankhorn Business Card</title>
<link rel="stylesheet" href="https://fonts.googleapis.com/css2?family=Work+Sans:wght@300;400;600;700&display=swap">
<style>
  :root {
    --page-bg: #eceeef;
    --card-black: #0e0e0f;
    --card-black-soft: #2a2b2d;
    --silver: #c9ccd1;
    --card-white: #ffffff;
    --brand-blue: #0aa3e6;
    --ink: #222426;
    --muted: #8a8f95;
    --divider: #bcd3dc;
    --net-pink: #f3c9d6;
    --net-blue: #d6e2ee;
  }
  * { margin: 0; padding: 0; box-sizing: border-box; }
  html, body {
    width: 1200px; height: 900px; overflow: hidden;
    background: var(--page-bg);
    font-family: "Work Sans", Arial, sans-serif;
  }
  .canvas {
    width: 1200px; height: 900px;
    display: flex; flex-direction: column; align-items: center; justify-content: center;
    gap: 40px;
  }
  .card {
    width: 660px; height: 377px;
    border-radius: 4px;
    box-shadow: 0 10px 30px rgba(0,0,0,0.14);
    position: relative; overflow: hidden;
  }
  /* Front */
  .card-front {
    background: var(--card-black);
    display: flex; align-items: center; justify-content: center;
  }
  .front-texture {
    position: absolute; inset: 0;
    background: linear-gradient(135deg, var(--card-black) 0%, var(--card-black-soft) 45%, var(--card-black) 100%);
    opacity: 0.8;
  }
  .front-brand {
    position: relative;
    display: flex; align-items: center; gap: 16px;
  }
  .brand-dot {
    width: 22px; height: 22px; border-radius: 50%;
    background: var(--silver);
  }
  .front-brand .brand-name {
    color: var(--silver);
    font-size: 46px; font-weight: 600; letter-spacing: 4px;
  }
  /* Back */
  .card-back {
    background: var(--card-white);
    display: flex;
  }
  .back-logo {
    width: 270px;
    display: flex; flex-direction: column; align-items: center; justify-content: center; gap: 18px;
  }
  .back-logo .brand-dot {
    width: 26px; height: 26px; background: var(--brand-blue);
  }
  .back-logo .brand-name {
    color: var(--brand-blue);
    font-size: 34px; font-weight: 400; letter-spacing: 2px;
  }
  .back-divider {
    width: 1px; margin: 60px 0; background: var(--divider);
  }
  .back-details {
    flex: 1; position: relative;
    padding: 78px 0 0 34px;
  }
  .network-backdrop {
    position: absolute; top: 0; right: 0; width: 260px; height: 100%;
    background: radial-gradient(ellipse at 70% 30%, var(--net-pink) 0%, rgba(243,201,214,0.25) 40%, transparent 70%),
                radial-gradient(ellipse at 40% 80%, var(--net-blue) 0%, transparent 60%);
    opacity: 0.7;
  }
  .person-name {
    position: relative;
    font-size: 44px; line-height: 1; color: var(--muted); font-weight: 300;
  }
  .person-name .first-name { color: var(--brand-blue); font-weight: 700; }
  .person-title {
    position: relative;
    margin-top: 8px; font-size: 18px; color: var(--muted); font-weight: 400;
  }
  .contact-list {
    position: relative; list-style: none; margin-top: 30px;
    display: flex; flex-direction: column; gap: 12px;
  }
  .contact-item {
    display: flex; align-items: center; gap: 12px;
    font-size: 17px; color: var(--ink);
  }
  .contact-item .value-strong { font-weight: 600; }
  .contact-icon { width: 20px; height: 20px; flex: none; }
</style>
</head>
<body>
<main class="canvas">
  <section class="card card-front" aria-label="Card front">
    <div class="front-texture" role="img" aria-label="Dark faceted triangle texture background"></div>
    <div class="front-brand">
      <span class="brand-dot"></span>
      <span class="brand-name">PLANKHORN</span>
    </div>
  </section>

  <section class="card card-back" aria-label="Card back">
    <div class="back-logo">
      <span class="brand-dot"></span>
      <span class="brand-name">PLANKHORN</span>
    </div>
    <div class="back-divider"></div>
    <div class="back-details">
      <div class="network-backdrop" role="img" aria-label="Soft pink and blue connected network line pattern"></div>
      <h1 class="person-name"><span class="first-name">Darrel</span> Sotho</h1>
      <p class="person-title">Managing Partner</p>
      <ul class="contact-list">
        <li class="contact-item">
          <svg class="contact-icon" viewBox="0 0 24 24" fill="none" stroke="#0aa3e6" stroke-width="2" stroke-linecap="round"><path d="M6 3h4l1 5-2.5 1.5a11 11 0 0 0 6 6L16 13l5 1v4a2 2 0 0 1-2 2A17 17 0 0 1 4 5a2 2 0 0 1 2-2z"/></svg>
          <span>Cell: <span class="value-strong">738-402-1954</span></span>
        </li>
        <li class="contact-item">
          <svg class="contact-icon" viewBox="0 0 24 24" fill="none" stroke="#0aa3e6" stroke-width="2"><circle cx="12" cy="12" r="9"/><path d="M3 12h18M12 3c3 3 3 15 0 18M12 3c-3 3-3 15 0 18"/></svg>
          <span>Web: Plankhorn.com</span>
        </li>
        <li class="contact-item">
          <svg class="contact-icon" viewBox="0 0 24 24" fill="none" stroke="#0aa3e6" stroke-width="2" stroke-linecap="round"><circle cx="12" cy="12" r="4"/><path d="M16 8v5a3 3 0 0 0 6 0v-1a10 10 0 1 0-4 8"/></svg>
          <span>Email: Darrel@Plankhorn.com</span>
        </li>
      </ul>
    </div>
  </section>
</main>
</body>
</html>
```